Mining and Labour hire business needs website

need a web page for a business located in country NSW,Australia. we provide labour hire with a background in electrical contracting. i've attached images that i would like used. and a text file with the text to be used

Target Market(s)

mining and resource sector

Industry/Entity Type

Business

Requirements
Must have
• my logo
• Pages: main, about us, labour hire services, electrical services, equipment, employment, contact us
Nice to have
• other photos/images of heavy industry/mining
• background photos in black and white would be good i think.
• photo sliders

```html
<!DOCTYPE html>
<html lang="en">
<head>
<meta charset="utf-8">
<title>Ridgeline Works</title>
<link rel="stylesheet" href="https://fonts.googleapis.com/css2?family=Oswald:wght@400;500&family=Roboto:wght@400;500;700&display=swap">
<style>
  :root {
    --gold: #c9a157;
    --gold-dark: #b08a44;
    --gold-light: #d4b06c;
    --ink: #222222;
    --text: #6a6a6a;
    --white: #ffffff;
    --pale: #efefef;
    --black: #111111;
  }
  * { box-sizing: border-box; margin: 0; padding: 0; }
  html, body { width: 670px; height: 1200px; overflow: hidden; background: var(--white); }
  body { font-family: 'Roboto', Arial, sans-serif; color: var(--text); }
  .page { position: relative; width: 670px; height: 1200px; overflow: hidden; }

  /* Header */
  .site-header { position: absolute; top: 0; left: 0; width: 670px; height: 56px; background: var(--white); }
  .brand { position: absolute; left: 50px; top: 16px; display: flex; align-items: center; gap: 8px; }
  .brand-square { width: 14px; height: 14px; background: var(--gold); }
  .brand-name { font-family: 'Oswald', sans-serif; font-weight: 500; font-size: 19px; color: var(--ink); letter-spacing: 0.5px; }
  .main-nav { position: absolute; right: 70px; top: 26px; display: flex; gap: 17px; font-size: 8px; color: var(--ink); letter-spacing: 0.2px; }
  .main-nav .active { color: var(--gold); }
  .search-btn { position: absolute; left: 600px; top: 22px; width: 21px; height: 20px; border: 1px solid #e2e2e2; display: flex; align-items: center; justify-content: center; }

  /* Hero */
  .hero { position: absolute; top: 56px; left: 0; width: 670px; height: 358px;
    background: radial-gradient(ellipse at 60% 30%, #c9c9c9 0%, #8f8f8f 45%, #4a4a4a 100%); }
  .hero-caption { position: absolute; left: 49px; top: 174px; width: 230px; height: 102px; background: rgba(20,20,20,0.82); padding: 14px 0 0 16px; }
  .hero-caption .lead { font-family: 'Oswald', sans-serif; font-size: 22px; color: var(--white); line-height: 1.2; }
  .hero-caption .big { font-family: 'Oswald', sans-serif; font-size: 38px; color: var(--gold); line-height: 1.2; letter-spacing: 0.5px; }
  .slider-arrows { position: absolute; left: 51px; top: 346px; display: flex; gap: 3px; }
  .slider-arrows span { width: 20px; height: 20px; border-radius: 50%; background: rgba(30,30,30,0.75); display: flex; align-items: center; justify-content: center; }

  /* Services band */
  .services { position: absolute; top: 414px; left: 0; width: 670px; height: 198px;
    background: linear-gradient(135deg, var(--gold-light), var(--gold) 55%, var(--gold-dark)); }
  .service { position: absolute; width: 160px; text-align: center; color: var(--white); }
  .service .icon { width: 52px; height: 52px; border: 1.5px solid var(--white); border-radius: 50%; margin: 0 auto; display: flex; align-items: center; justify-content: center; }
  .service h3 { font-weight: 500; font-size: 11px; margin-top: 12px; letter-spacing: 0.3px; }
  .service p { font-size: 6.2px; line-height: 10.5px; margin-top: 7px; }
  .ghost-btn { display: inline-block; margin-top: 9px; border: 1px solid var(--white); border-radius: 3px; padding: 4px 9px; font-size: 6px; color: var(--white); }

  /* Welcome */
  .welcome { position: absolute; top: 612px; left: 0; width: 670px; height: 216px; background: var(--white); }
  .video-frame { position: absolute; left: 49px; top: 29px; width: 242px; height: 150px; border: 1px solid #dcdcdc; padding: 3px; background: var(--white); }
  .video-still { position: relative; width: 100%; height: 100%;
    background: linear-gradient(170deg, #5e86b0 0%, #9bb1c4 18%, #c2561b 35%, #a8461a 70%, #3a2a20 100%); }
  .play { position: absolute; left: 50%; top: 50%; width: 44px; height: 44px; margin: -22px 0 0 -22px; border-radius: 50%; background: rgba(60,60,60,0.75); display: flex; align-items: center; justify-content: center; }
  .welcome-copy { position: absolute; left: 310px; top: 33px; width: 312px; }
  .welcome-copy h2 { font-weight: 400; font-size: 13px; color: var(--gold); }
  .welcome-copy h4 { font-weight: 400; font-size: 9.5px; color: var(--ink); margin-top: 6px; }
  .welcome-copy p { font-size: 6.4px; line-height: 11.8px; margin-top: 8px; }
  .gold-btn { display: inline-block; background: var(--gold); color: var(--white); font-size: 6.5px; font-weight: 500; padding: 5px 13px; border-radius: 2px; box-shadow: 0 1px 0 var(--gold-dark); }
  .welcome-copy .gold-btn { margin-top: 14px; }

  /* What we do */
  .what-we-do { position: absolute; top: 828px; left: 3px; width: 667px; height: 202px; background: linear-gradient(180deg, var(--pale), #e6e6e6); }
  .what-we-do h2 { position: absolute; left: 47px; top: 36px; font-weight: 400; font-size: 13px; color: var(--gold); }
  .what-we-do p { position: absolute; left: 47px; top: 66px; width: 372px; font-size: 6.4px; line-height: 13.6px; }
  .what-we-do .gold-btn { position: absolute; left: 47px; top: 146px; }
  .wwd-brand { position: absolute; left: 455px; top: 82px; display: flex; align-items: center; gap: 8px; }
  .wwd-brand .brand-square { width: 18px; height: 18px; }
  .wwd-brand .brand-name { font-size: 24px; }

  /* Footer */
  .site-footer { position: absolute; top: 1030px; left: 0; width: 670px; height: 132px; background: var(--gold); color: var(--white); }
  .footer-col { position: absolute; top: 28px; }
  .footer-col h5 { font-weight: 400; font-size: 10px; letter-spacing: 0.2px; }
  .footer-col p, .footer-col li { font-size: 6.4px; line-height: 9px; }
  .newsletter p { margin-top: 8px; width: 130px; }
  .email-field { margin-top: 6px; width: 120px; height: 17px; background: #f2f2f2; border: 1px solid #cfcfcf; color: #555; font-size: 6.3px; padding: 4px 6px; }
  .subscribe { display: inline-block; margin-top: 6px; background: var(--black); color: var(--white); font-size: 6.3px; padding: 4px 8px; border-radius: 2px; }
  .tweet { display: flex; gap: 6px; margin-top: 8px; }
  .tweet .dot { width: 8px; height: 8px; border-radius: 50%; background: var(--white); margin-top: 1px; flex: none; }
  .tweet p { margin-top: 0; }
  .tweet em { font-style: italic; }
  .contact p { margin-top: 6px; }
  .contact p + p { margin-top: 10px; }
  .social ul { list-style: none; margin-top: 9px; }
  .social li { display: flex; align-items: center; gap: 10px; margin-bottom: 6px; }
  .social .ring { width: 18px; height: 18px; border: 1px solid var(--white); border-radius: 50%; }

  .copyright { position: absolute; top: 1162px; left: 0; width: 670px; height: 38px; background: var(--black); color: var(--white); font-size: 6.5px; text-align: center; line-height: 38px; }
</style>
</head>
<body>
<div class="page">

  <header class="site-header">
    <div class="brand"><span class="brand-square"></span><span class="brand-name">Ridgeline Works</span></div>
    <nav class="main-nav">
      <span class="active">HOME</span><span>SERVICES</span><span>PORTFOLIO</span><span>SOLUTIONS</span><span>JOBS</span><span>BLOG</span><span>CONTACTS</span>
    </nav>
    <div class="search-btn">
      <svg width="8" height="8" viewBox="0 0 10 10"><circle cx="4" cy="4" r="3" fill="none" stroke="#222" stroke-width="1.5"/><line x1="6.2" y1="6.2" x2="9" y2="9" stroke="#222" stroke-width="1.5"/></svg>
    </div>
  </header>

  <section class="hero" role="img" aria-label="Black and white photo of large steel gears with an engineer in a hard hat pointing upward">
    <div class="hero-caption">
      <div class="lead">We start work with</div>
      <div class="big">GREAT VISION</div>
    </div>
    <div class="slider-arrows">
      <span><svg width="8" height="8" viewBox="0 0 8 8"><polyline points="5,1 2,4 5,7" fill="none" stroke="#fff" stroke-width="1.3"/></svg></span>
      <span><svg width="8" height="8" viewBox="0 0 8 8"><polyline points="3,1 6,4 3,7" fill="none" stroke="#fff" stroke-width="1.3"/></svg></span>
    </div>
  </section>

  <section class="services">
    <div class="service" style="left:54px; top:30px;">
      <div class="icon">
        <svg width="20" height="18" viewBox="0 0 20 18"><rect x="1" y="1" width="18" height="12" rx="1" fill="none" stroke="#fff" stroke-width="2"/><rect x="8" y="13" width="4" height="3" fill="#fff"/><rect x="5" y="16" width="10" height="1.5" fill="#fff"/></svg>
      </div>
      <h3>PLANING</h3>
      <p>Lorem Ipsum has been the industry's standard dummy text ever since the 1500s, when an unknown printer took a galley of type and scrambled book</p>
      <span class="ghost-btn">Read More &#9656;</span>
    </div>
    <div class="service" style="left:254px; top:32px;">
      <div class="icon">
        <svg width="20" height="18" viewBox="0 0 20 18"><polygon points="1,8 19,1 13,17 9,10" fill="#fff"/></svg>
      </div>
      <h3>DESIGN</h3>
      <p>Lorem Ipsum has been the industry's standard dummy text ever since the 1500s, when an unknown printer took a galley of type and scrambled book</p>
      <span class="ghost-btn">Read More &#9656;</span>
    </div>
    <div class="service" style="left:456px; top:30px;">
      <div class="icon">
        <svg width="20" height="16" viewBox="0 0 20 16"><rect x="3" y="2" width="14" height="9" fill="none" stroke="#fff" stroke-width="1.6"/><rect x="1" y="12" width="18" height="2" fill="#fff"/></svg>
      </div>
      <h3>CODING</h3>
      <p>Lorem Ipsum has been the industry's standard dummy text ever since the 1500s, when an unknown printer took a galley of type and scrambled book</p>
      <span class="ghost-btn">Read More &#9656;</span>
    </div>
  </section>

  <section class="welcome">
    <div class="video-frame">
      <div class="video-still" role="img" aria-label="Video still of a rust-orange industrial mine building against a blue sky">
        <span class="play"><svg width="16" height="18" viewBox="0 0 16 18"><polygon points="2,1 15,9 2,17" fill="#fff"/></svg></span>
      </div>
    </div>
    <div class="welcome-copy">
      <h2>WELCOME TO RIDGELINEWORKS</h2>
      <h4>Neque porro quisquam est qui dolorem ipsum quia dolor sit amet</h4>
      <p>Lorem Ipsum has been the industry's standard dummy text ever since the 1500s, when an unknown printer took a galley of type and scrambled it to make a type specimen book. It has survived not only five centuries, but also the leap into electronic typesetting, remaining essentially unchanged.</p>
      <p>It was popularised in the 1960s with the release of Typeline sheets containing Lorem Ipsum passages, and more recently with desktop publishing software like PageComposer including versions</p>
      <span class="gold-btn">READ MORE</span>
    </div>
  </section>

  <section class="what-we-do">
    <h2>WHAT WE DO</h2>
    <p>Lorem Ipsum has been the industry's standard dummy text ever since the 1500s, when an unknown printer took a galley of type and scrambled it to make a type specimen book. It has survived not only five centuries, but also the leap into electronic typesetting, remaining essentially unchanged. It was popularised in the 1960s with the release of Typeline sheets containing Lorem Ipsum passages, and more recently with desktop publishing software like PageComposer including versions of Lorem Ipsum</p>
    <span class="gold-btn">READ MORE</span>
    <div class="wwd-brand"><span class="brand-square"></span><span class="brand-name">Ridgeline Works</span></div>
  </section>

  <footer class="site-footer">
    <div class="footer-col newsletter" style="left:52px;">
      <h5>NEWSLETTERS SIGN UP</h5>
      <p>Sign up for our daily email by entering your information below</p>
      <div class="email-field">Email address</div>
      <span class="subscribe">SUBSCRIBE</span>
    </div>
    <div class="footer-col" style="left:218px;">
      <h5>LATEST TWEET</h5>
      <div class="tweet" style="margin-top:12px;"><span class="dot"></span><p>Featured Workspace : Ironbay<br>rdgl.io/7Hk2Vq <em>10 hours ago</em></p></div>
      <div class="tweet" style="margin-top:14px;"><span class="dot"></span><p>Featured Workspace : Ironbay<br>rdgl.io/7Hk2Vq <em>10 hours ago</em></p></div>
    </div>
    <div class="footer-col contact" style="left:385px;">
      <h5>GET IN TOUCH</h5>
      <p style="margin-top:12px;">Address : 42 Quarry Road,<br>Millbrook, NSW</p>
      <p>Phone : 02 6180 4417</p>
      <p>Email : hello@ridgelineworks.example</p>
    </div>
    <div class="footer-col social" style="left:541px;">
      <h5>FOLLOW US ON</h5>
      <ul>
        <li><span class="ring"></span>Linkwall</li>
        <li><span class="ring"></span>Chirper</li>
        <li><span class="ring"></span>Photoline</li>
      </ul>
    </div>
  </footer>

  <div class="copyright">Copyright © 2015. All Rights Reserved</div>
</div>
</body>
</html>
```